依頼詳細
現在木曜日のみ休診となっていますが、獣医が一人増えることにより2020年2月1日より全曜日で診察を行うことを予定しています(盆、年末年始、GW除く)。
その告知をするためのチラシをポスティング、新聞折り込みで配布する予定で、その告知チラシのデザインをお願いしたいです。表面は動物病院の告知で、裏面は併設のトリミングサロンの宣伝をしたいと思っています。思わず引きつかれるようなデザインをお願いしたいです。
(表面)
・添付のミドリツバメ便の画像のイメージで「木曜日休診」が「全曜日診察」(盆、年末年始、GWは除く)へ変わることを告知したいです
・キャラクターは犬と猫のイラストでお願いしたいです
・全体的なデザインはシンプルで遊び心があるものにしてほしいです
・看板(暖簾)の写真(添付)も載せてほしいです(これは小さくてよいです)
(裏面)
・犬が猫足バスタブに浸かって、楽しそうにしているイメージでお願いします
・こちらもシンプルで遊び心のあるデザインでお願いしたいです
・トリミングは「シャンプーのみ」、「シャンプー&カット」のコースがあり、両コースに爪切り、足裏バリカン、耳掃除、お腹バリカン、肛門バリカン、肛門嚢絞りを含むことを記載してほしいです
・動物病院併設なのでシニア犬、持病持ちの犬も対応可能と載せてほしいです
・看板(暖簾)の写真(添付)も載せてほしいです(これも小さくてよいです)
記載項目
【表面】
動物病院ひだまり 若草台
京都市西京区小川原南町17 メゾン葵野2階
電話番号 0756147328
診察時間 午前9:30~12:30 予約診察16:00~16:45 午後17:00~20:00
(日、祝日は午前のみ)
全曜日診察(盆、正月、GWは除く)
獣医師名 院長 青柳航平 副院長 村瀬譲
駐車場5台完備(トリミングサロン共用)
駐車場地図(添付)
【裏面】
トリミングサロン凛(動物病院ひだまり 若草台 併設)
電話番号 0756281945
営業時間 9:00~18:00
店休日 木曜日 日曜日
店長名 北條葉月
駐車場5台完備(動物病院共用)
ペットホテル完備
トリミング料金 (税抜き)
・トイプードル シャンプー3780円~ シャンプー&カット6480円~
・チワワ シャンプー2980円~ シャンプー&カット4480円~
・ヨークシャーテリア シャンプー3280円~ シャンプー&カット5780円~
その他全犬種対応可能
ペットホテル料金(1泊2日、税抜き)
・小型犬 2980円 ・中型犬 3980円 ・大型犬 4980円
一時預かりも可能
サイズ
A3
ページ数
両面
希望イメージ
シンプル 複雑
単色 カラフル
暗い 明るい
日常 高級
遊び心 厳粛
未来的 伝統的
女性的 男性的
希望する色
黄・オレンジ系、緑系、茶系
納品ファイル
補足説明
手直しのやり取りは基本的に少なく(5回以下に)したいと思いますが、納得のいくものを制作していただきたいので、出来れば制限を設けないようにしてもらいたいです

診察表を使った表現が、病院であることが分かりやすく気に入りました。

この度はコンペに応募していただきありがとうございました。

```html
<!DOCTYPE html>
<html lang="ja">
<head>
<meta charset="utf-8">
<title>動物病院ひだまり 若草台 全曜日診察のお知らせ</title>
<link rel="stylesheet" href="https://fonts.googleapis.com/css2?family=M+PLUS+Rounded+1c:wght@500;700;800;900&family=Noto+Sans+JP:wght@400;500;700;900&display=swap">
<style>
  :root {
    --cream: #fbf1d6;
    --cream-deep: #f3e2b6;
    --brown: #6a4a2e;
    --brown-dark: #4e3520;
    --tan: #c9a77a;
    --orange: #f08419;
    --green: #7bab36;
    --white: #ffffff;
    --ink: #3b2a1c;
  }
  * { margin: 0; padding: 0; box-sizing: border-box; }
  html, body { width: 846px; height: 1200px; overflow: hidden; background: var(--white); }
  body { font-family: "Noto Sans JP", sans-serif; color: var(--ink); }
  .flyer { position: relative; width: 846px; height: 1200px; overflow: hidden; background: var(--cream); }

  .paw-backdrop { position: absolute; left: 0; top: 0; width: 846px; height: 700px;
    background: linear-gradient(180deg, var(--cream) 0%, var(--cream-deep) 100%); }

  .brand { position: absolute; left: 14px; top: 14px; display: flex; align-items: center; gap: 8px; }
  .brand-mark { width: 32px; height: 32px; background: var(--brown); border-radius: 4px; flex: none; }
  .brand-text { display: flex; flex-direction: column; }
  .brand-name { font-family: "M PLUS Rounded 1c", sans-serif; font-weight: 800; font-size: 15px; line-height: 1.2; color: var(--brown); white-space: nowrap; }
  .brand-sub { font-family: "M PLUS Rounded 1c", sans-serif; font-weight: 800; font-size: 7px; color: var(--brown); letter-spacing: .04em; white-space: nowrap; }

  .news-bubble { position: absolute; left: 612px; top: 20px; width: 220px; height: 54px;
    background: var(--white); border: 3px solid var(--brown); border-radius: 28px;
    display: flex; align-items: center; justify-content: center;
    font-family: "M PLUS Rounded 1c", sans-serif; font-weight: 800; font-size: 18px; color: var(--brown); white-space: nowrap; }
  .news-bubble svg { position: absolute; left: 14px; bottom: -15px; }

  .mascots { position: absolute; left: 248px; top: 40px; width: 352px; height: 206px;
    background: linear-gradient(90deg, #6f737a 0%, #8a8d92 45%, #c98a3c 55%, #8a5a2e 100%);
    border-radius: 110px 110px 10px 10px; }

  .announce-card { position: absolute; left: 100px; top: 240px; width: 648px; height: 318px;
    background: var(--white); border: 4px solid var(--brown); border-radius: 10px; text-align: center; }
  .announce-date { margin-top: 22px; font-weight: 700; font-size: 21px; line-height: 1.3; color: var(--brown); letter-spacing: .04em; }
  .announce-before { margin-top: 4px; font-family: "M PLUS Rounded 1c", sans-serif; font-weight: 900; font-size: 36px; line-height: 1.2; color: var(--brown-dark); letter-spacing: .06em; }
  .announce-before small { font-size: 22px; font-weight: 800; }
  .announce-after { margin-top: 10px; font-family: "M PLUS Rounded 1c", sans-serif; font-weight: 900; font-size: 108px; line-height: 1; color: var(--orange); letter-spacing: .06em; white-space: nowrap; }
  .announce-foot { position: absolute; left: 20px; right: 20px; top: 262px; display: flex; align-items: center; gap: 12px; white-space: nowrap; }
  .merit { font-weight: 900; font-size: 22px; color: var(--white); padding: 2px 14px; border-radius: 4px; }
  .merit--safe { background: var(--orange); }
  .merit--easy { background: var(--green); margin-right: 22px; }
  .announce-possible { font-family: "M PLUS Rounded 1c", sans-serif; font-weight: 800; font-size: 24px; color: var(--brown); }
  .announce-possible small { font-size: 12px; font-weight: 700; }

  .hours-aside { position: absolute; right: 98px; top: 562px; font-size: 11px; color: var(--brown); white-space: nowrap; }
  .hours { position: absolute; left: 100px; top: 578px; width: 648px; }
  .hours-head { height: 26px; background: var(--brown); color: var(--white);
    font-weight: 700; font-size: 15px; text-align: center; line-height: 26px; border-radius: 3px 3px 0 0; }
  .hours-rows { display: flex; justify-content: space-between; align-items: center; background: var(--white);
    border: 2px solid var(--brown); border-top: none; height: 48px; padding: 0 10px; }
  .slot { display: flex; align-items: center; gap: 6px; white-space: nowrap; }
  .slot-label { font-weight: 900; font-size: 15px; color: var(--white); padding: 2px 7px; border-radius: 3px; }
  .slot-label--am, .slot-label--pm { background: var(--orange); }
  .slot-label--booked { background: var(--green); }
  .slot-time { font-family: "M PLUS Rounded 1c", sans-serif; font-weight: 900; font-size: 20px; color: var(--brown-dark); }
  .hours-note { margin-top: 5px; font-size: 10px; color: var(--brown); white-space: nowrap; }

  .motto-band { position: absolute; left: 0; top: 700px; width: 846px; height: 32px; background: var(--brown);
    color: var(--white); font-weight: 700; font-size: 17px; line-height: 32px; text-align: center; letter-spacing: .04em; }

  .clinic-info { position: absolute; left: 0; top: 732px; width: 846px; height: 116px; background: var(--tan); }
  .clinic-name { position: absolute; left: 20px; top: 12px; background: var(--white); color: var(--brown);
    font-weight: 900; font-size: 20px; padding: 2px 12px; border-radius: 3px; white-space: nowrap; }
  .clinic-phone { position: absolute; left: 318px; top: 4px; display: flex; align-items: center; gap: 6px;
    font-family: "M PLUS Rounded 1c", sans-serif; font-weight: 900; font-size: 34px; color: var(--brown-dark); white-space: nowrap; }
  .clinic-meta { position: absolute; left: 20px; top: 56px; width: 680px; font-size: 12px; line-height: 1.5; color: var(--brown-dark); font-weight: 500; white-space: nowrap; }
  .clinic-meta b { font-weight: 700; }
  .vet-photo { position: absolute; left: 716px; top: 8px; width: 112px; height: 100px;
    background: linear-gradient(180deg, #e7dccb 0%, #b8a58a 100%); }

  .access { position: absolute; left: 0; top: 848px; width: 846px; height: 352px; background: var(--white); }
  .access-notes { position: absolute; left: 20px; top: 12px; width: 806px; font-size: 11px; line-height: 1.6; color: var(--brown-dark); }
  .sign-photo { position: absolute; left: 20px; top: 64px; width: 196px; height: 272px;
    background: linear-gradient(180deg, #7b6048 0%, #4a3a2c 100%); border-radius: 4px; }
  .sign-caption { position: absolute; left: 230px; top: 70px; width: 160px; font-size: 12px; line-height: 1.7; color: var(--brown); }
  .map-caption { position: absolute; left: 230px; top: 150px; width: 160px; display: flex; align-items: center; gap: 6px;
    font-size: 12px; font-weight: 700; line-height: 1.5; color: var(--brown); }
  .parking-badge { flex: none; width: 26px; height: 26px; background: var(--green); color: var(--white); border-radius: 4px;
    font-weight: 900; font-size: 17px; display: flex; align-items: center; justify-content: center; }
  .parking-map { position: absolute; left: 404px; top: 64px; width: 424px; height: 272px;
    background: linear-gradient(135deg, #f2efe8 0%, #e2ddd2 100%); border: 2px solid var(--brown); border-radius: 4px; }
</style>
</head>
<body>
<main class="flyer">
  <div class="paw-backdrop" role="img" aria-label="肉球模様の背景"></div>

  <header class="brand">
    <span class="brand-mark"></span>
    <span class="brand-text">
      <span class="brand-name">動物病院ひだまり 若草台</span>
      <span class="brand-sub">HIDAMARI WAKAKUSA ANIMAL HOSPITAL</span>
    </span>
  </header>

  <div class="mascots" role="img" aria-label="カードの上から顔をのぞかせる猫と犬のイラスト"></div>

  <div class="news-bubble">獣医が一人増えました！
    <svg width="26" height="18" viewBox="0 0 26 18"><path d="M2 0 L24 0 L4 16 Z" fill="#ffffff" stroke="#6a4a2e" stroke-width="3" stroke-linejoin="round"/><rect x="0" y="0" width="26" height="3" fill="#ffffff"/></svg>
  </div>

  <section class="announce-card">
    <p class="announce-date">2020年2月1日より</p>
    <p class="announce-before">木曜日休診<small>から</small></p>
    <h1 class="announce-after">全曜日診察</h1>
    <div class="announce-foot">
      <span class="merit merit--safe">安心</span>
      <span class="merit merit--easy">便利</span>
      <span class="announce-possible">可能になります！<small>（盆、年末年始、GWは除く）</small></span>
    </div>
  </section>

  <p class="hours-aside">※日、祝日は午前のみ</p>
  <section class="hours">
    <div class="hours-head">診察時間</div>
    <div class="hours-rows">
      <div class="slot"><span class="slot-label slot-label--am">午前</span><span class="slot-time">9:30～12:30</span></div>
      <div class="slot"><span class="slot-label slot-label--booked">予約診察</span><span class="slot-time">16:00～16:45</span></div>
      <div class="slot"><span class="slot-label slot-label--pm">午後</span><span class="slot-time">17:00～20:00</span></div>
    </div>
    <p class="hours-note">※予約はお電話にてご連絡下さい。予約は前日までに受け付けております。</p>
  </section>

  <div class="motto-band">すべては動物の健康のために、来てよかったと思える診察を</div>

  <section class="clinic-info">
    <div class="clinic-name">動物病院ひだまり 若草台</div>
    <div class="clinic-phone">
      <svg width="28" height="28" viewBox="0 0 24 24"><path d="M6.6 10.8a15.1 15.1 0 0 0 6.6 6.6l2.2-2.2a1 1 0 0 1 1-.25 11.4 11.4 0 0 0 3.6.57 1 1 0 0 1 1 1V20a1 1 0 0 1-1 1A17 17 0 0 1 3 4a1 1 0 0 1 1-1h3.5a1 1 0 0 1 1 1c0 1.25.2 2.45.57 3.57a1 1 0 0 1-.25 1z" fill="#4e3520"/></svg>
      075-614-7328
    </div>
    <div class="clinic-meta">
      京都市西京区小川原南町17 メゾン葵野2階　<b>【院長】</b>青柳航平　<b>【副院長】</b>村瀬譲<br>
      <b>HP：</b>https://hidamari-wakakusa.jp/　<b>【駐車場】</b>5台完備（トリミングサロン共用）<br>
      <b>【休診日】</b>盆、年末年始、GW　<b>【併設】</b>トリミングサロン凛
    </div>
    <div class="vet-photo" role="img" aria-label="院長の写真"></div>
  </section>

  <section class="access">
    <p class="access-notes">【診察対象】犬・猫・うさぎ・小動物　【予約】前日までにお電話ください<br>【併設】トリミングサロン凛（シニア犬・持病のある子も対応）</p>
    <div class="sign-photo" role="img" aria-label="病院入口の看板と暖簾の写真"></div>
    <p class="sign-caption">入口の暖簾が目印です。<br>お気軽にお立ち寄りください。</p>
    <div class="map-caption"><span class="parking-badge">P</span>駐車場5台完備<br>（トリミングサロン共用）</div>
    <div class="parking-map" role="img" aria-label="病院と駐車場の周辺地図"></div>
  </section>
</main>
</body>
</html>
```